Penny Harvest

Logo and general packaging design for premium quality, price conscious super foods.

Initial product portfolio includes:

Organic Raw Chia Seeds - Resealable plastic bags with 3 x 5 label.
Organic Cold Pressed Coconut Oil (plastic jar) - 2.5 x 6.5 label

The design should be transferable to additional products.

Project requirements:

The design should be simple and the core trade dress should be no more than 2 or 3 colors. The logo should reproduce well in black/1 color.

The idea of this design is to convey quality and simplicity, like a "no frills", premium quality brand.

Deliverable: fully editable (text and illustration):

Logo.

Basic Jar label design.

Basic Bag label design.

Target Market(s)

Educated women aged 22-45

Industry/Entity Type

Plastic

Requirements
Must have
• Clear, simple logo, delivered in vector form, 1 color/black.
• Use of logo on 1 jar label and 1 bag label, each with product name and space for required and optional marketing content.
Nice to have
• Additional iterations of the design to demonstrate your concept of how we will visually vary additional items in jars and bags.
• i.e. What an additional product in a bag would look like for purposes of brand consistency and product differentiation on shelf or online in e-store.
Should not have
• overly detailed graphics that don't scale well and/or may be hard to read or understand. 4 color design elements (except to simiulate how the product may look through the clear jar or bag or how the product may be placed in a simulated surrounding or ad.

```html
<!DOCTYPE html>
<html lang="en">
<head>
<meta charset="utf-8">
<title>Penny Harvest — Label System</title>
<link rel="stylesheet" href="https://fonts.googleapis.com/css2?family=Arimo:wght@400;700&display=swap">
<style>
  :root {
    --brand-green: #1d6b4c;
    --label-cream: #f8f6e3;
    --ink: #111111;
    --paper: #ffffff;
    --stage: #f1f1ef;
  }
  * { box-sizing: border-box; margin: 0; padding: 0; }
  html, body { width: 1200px; height: 1053px; overflow: hidden; }
  body {
    background: var(--stage);
    font-family: "Arimo", Arial, sans-serif;
    color: var(--ink);
    position: relative;
  }

  /* Bag label: 3 x 5 */
  .bag-label {
    position: absolute;
    left: 110px;
    top: 220px;
    width: 440px;
    height: 600px;
    border-radius: 22px;
    overflow: hidden;
    background: var(--label-cream);
    box-shadow: 0 2px 10px rgba(0,0,0,0.12);
  }
  .bag-label .brand-band {
    height: 205px;
    background: var(--brand-green);
    padding: 58px 0 0 26px;
  }
  .bag-label .brand-name { font-size: 50px; }
  .bag-label .product-name {
    padding: 30px 26px 0;
    font-size: 37px;
    line-height: 1.12;
    font-weight: 400;
  }

  /* Jar label: 2.5 x 6.5 */
  .jar-label {
    position: absolute;
    left: 640px;
    top: 380px;
    width: 470px;
    height: 310px;
    background: var(--label-cream);
    box-shadow: 0 2px 10px rgba(0,0,0,0.12);
  }
  .jar-label .brand-band {
    height: 150px;
    background: var(--brand-green);
    padding: 40px 0 0 28px;
  }
  .jar-label .brand-name { font-size: 44px; }
  .jar-label .product-name {
    padding: 26px 28px 0;
    font-size: 33px;
    line-height: 1.15;
    font-weight: 400;
  }

  .brand-name {
    color: var(--paper);
    font-weight: 700;
    line-height: 0.95;
    letter-spacing: -0.5px;
  }

  /* Nutrition panel */
  .nutrition-panel {
    position: absolute;
    left: 26px;
    bottom: 30px;
    width: 170px;
    background: var(--paper);
    border: 1px solid var(--ink);
    padding: 3px 4px;
    font-size: 6px;
    line-height: 1.35;
  }
  .nutrition-panel .panel-title {
    font-size: 13px;
    font-weight: 700;
    line-height: 1.05;
    border-bottom: 1px solid var(--ink);
    padding-bottom: 1px;
  }
  .nutrition-panel .row {
    display: flex;
    justify-content: space-between;
    border-bottom: 0.5px solid #777;
  }
  .nutrition-panel .row.thick { border-bottom: 3px solid var(--ink); }
  .nutrition-panel .row.indent span:first-child { padding-left: 6px; }
  .nutrition-panel b { font-weight: 700; }
  .nutrition-panel .footnote { font-size: 5px; line-height: 1.25; padding-top: 1px; }
  .nutrition-panel .source {
    margin-top: 2px;
    text-align: center;
    background: #e6e6e6;
    font-size: 5px;
  }
</style>
</head>
<body>

  <section class="bag-label" aria-label="Chia seeds bag label">
    <div class="brand-band">
      <div class="brand-name">Penny<br>Harvest</div>
    </div>
    <h1 class="product-name">Organic Raw<br>Chia Seeds.</h1>

    <div class="nutrition-panel">
      <div class="panel-title">Nutrition Facts</div>
      <div class="row thick"><span>Serving Size 1 oz (28g)</span></div>
      <div class="row"><span><b>Amount Per Serving</b></span></div>
      <div class="row"><span><b>Calories</b> 137</span><span>Calories from Fat 78</span></div>
      <div class="row"><span></span><span><b>% Daily Value*</b></span></div>
      <div class="row"><span><b>Total Fat</b> 9g</span><span>14%</span></div>
      <div class="row indent"><span>Saturated Fat 1g</span><span>5%</span></div>
      <div class="row indent"><span>Trans Fat 0g</span><span></span></div>
      <div class="row"><span><b>Cholesterol</b> 0mg</span><span>0%</span></div>
      <div class="row"><span><b>Sodium</b> 5mg</span><span>0%</span></div>
      <div class="row"><span><b>Total Carbohydrate</b> 12g</span><span>4%</span></div>
      <div class="row indent"><span>Dietary Fiber 10g</span><span>40%</span></div>
      <div class="row indent"><span>Sugars 0g</span><span></span></div>
      <div class="row thick"><span><b>Protein</b> 4g</span><span></span></div>
      <div class="row"><span>Vitamin A 0%</span><span>Vitamin C 3%</span></div>
      <div class="row"><span>Calcium 18%</span><span>Iron 12%</span></div>
      <div class="footnote">*Percent Daily Values are based on a 2,000 calorie diet.</div>
      <div class="source">Nutrition data per serving</div>
    </div>
  </section>

  <section class="jar-label" aria-label="Coconut oil jar label">
    <div class="brand-band">
      <div class="brand-name">Penny<br>Harvest</div>
    </div>
    <h1 class="product-name">Organic Cold Pressed<br>Coconut Oil.</h1>
  </section>

</body>
</html>
```